Clean Chic Simple Black & White One sided Biz Card

I need a business card for my company Brief Matter Arrangers. We are a luxury, white glove service for organizing files for attorneys.
I would like something that is stunningly simple and chic/sexy. This is going to be only one sided. We are going to use raised ink or ink embossing for the printing. So the logo will be raised in black. I am currently waiting to hear back from the printer as to whether or not the logo has to be in all black or can be left in its current state of black with grey initials. Please check our website for inspiration. www.briefmatterarrangers.example.
Thank you so much for your time.

* Please decide whichever title you think looks best(Chief Executive Officer, CEO, or President)
Updates

I really like the designs that make the logo large and the main focus.  
I also like the use of modern, masculine, simple, chic fonts for the slogan and info.

1) No bold font on slogan or info
2) Shrink info to be smaller maybe to make the logo bigger and more the focus
3) Maybe use grey for all the info and slogan so the focus will be on the logo

Thank you so much for your time!!

Target Market(s)

Luxury driven lawyers and their support staff

Industry/Entity Type

Printer

Requirements
Must have
• One sided card

Modern, sleek, masculine, chic, simple font.

Please add our slogan. Refer to file labeled "old logo" to see how we added our slogan under the old logo.
The slogan is, "We Bring Calm to the Case Binder"

Please include the info below:
Marion Tullbeck (Chief Executive Officer, CEO, or President)
812 North Halvering Avenue, Suite 1400
Los Angeles, California 90071
P: (213)555-0182 F: (213)555-0167
mariont@briefmatterarrangers.example
www.briefmatterarrangers.example

Please refer to attached file labeled "inkpressingembossing requirements" for requirements from my printer. Thank you!
Nice to have
• It can be super simple with just the logo and my info. Or it could maybe have some cool feature. Just clean please.

I would prefer the info not be in bold. I think this will help the Logo stand out as the main focus.

I attached files of how the ink pressing and embossing will look.
Should not have
• No crazy shapes and no color other than black with a white background. The logo should be the focus since it will be embossed.

```html
<!DOCTYPE html>
<html lang="en">
<head>
<meta charset="utf-8">
<title>Brief Matter Arrangers, Inc. — Business Card</title>
<link rel="stylesheet" href="https://fonts.googleapis.com/css2?family=Cormorant+Garamond:wght@500&family=Gilda+Display&family=Josefin+Sans:wght@300&family=Playfair+Display+SC:wght@900&display=swap">
<style>
  :root {
    --paper: #ffffff;
    --ink: #111111;
    --mark-grey: #a6b3b6;
    --info-ink: #2b2b2b;
  }
  html, body {
    margin: 0;
    padding: 0;
    width: 1200px;
    height: 686px;
    overflow: hidden;
    background: var(--paper);
  }
  .card {
    position: relative;
    width: 1200px;
    height: 686px;
    background: var(--paper);
    color: var(--ink);
  }
  .brand-mark {
    position: absolute;
    left: 0;
    right: 0;
    top: 178px;
    text-align: center;
    font-family: "Cormorant Garamond", Georgia, serif;
    font-weight: 500;
    font-style: normal;
    font-size: 76px;
    line-height: 1;
    color: var(--mark-grey);
    margin: 0;
  }
  .company-name {
    position: absolute;
    left: 0;
    right: 0;
    top: 302px;
    text-align: center;
    font-family: "Playfair Display SC", "Bodoni Moda", serif;
    font-weight: 900;
    font-size: 42px;
    letter-spacing: 0.24em;
    line-height: 1;
    margin: 0;
    padding-left: 0.24em;
  }
  .slogan {
    position: absolute;
    left: 0;
    right: 0;
    top: 362px;
    text-align: center;
    font-family: "Josefin Sans", Arial, sans-serif;
    font-weight: 300;
    font-style: normal;
    font-size: 23px;
    letter-spacing: 0.06em;
    color: var(--info-ink);
    margin: 0;
  }
  .contact {
    position: absolute;
    top: 450px;
    font-style: normal;
    font-size: 21px;
    line-height: 29px;
    color: var(--info-ink);
    margin: 0;
  }
  .contact-person {
    right: 643px;
    text-align: right;
    font-family: "Josefin Sans", Arial, sans-serif;
    font-weight: 300;
  }
  .contact-person .name,
  .contact-person .title {
    letter-spacing: 0.08em;
    font-size: 22px;
  }
  .contact-office {
    left: 598px;
    text-align: left;
    font-family: "Gilda Display", Georgia, serif;
    font-weight: 400;
    font-size: 21px;
  }
  .contact span { display: block; }
  .divider {
    position: absolute;
    left: 574px;
    top: 434px;
    width: 3px;
    height: 157px;
    background: var(--ink);
  }
</style>
</head>
<body>
  <main class="card">
    <p class="brand-mark">Brief Matter Arrangers</p>
    <h1 class="company-name">BRIEF MATTER ARRANGERS, INC.</h1>
    <p class="slogan">"WE BRING CALM TO THE CASE BINDER"</p>

    <address class="contact contact-person">
      <span class="name">MARION TULLBECK</span>
      <span class="title">CHIEF EXECUTIVE OFFICER</span>
      <span class="web">www.briefmatterarrangers.example</span>
      <span class="email">mariont@briefmatterarrangers.example</span>
    </address>

    <div class="divider" aria-hidden="true"></div>

    <address class="contact contact-office">
      <span class="street">812 North Halvering Avenue, Suite 1400,</span>
      <span class="city">Los Angeles, California 90071</span>
      <span class="phone">P: (213)555-0182</span>
      <span class="fax">F: (213)555-0167</span>
    </address>
  </main>
</body>
</html>
```